Stationary for Home Builder
Larkfield Dwellings Inc.
Project: Stationary for Home Builder
Stationary for Home Builder - Construction
Creative Brief
Modern
Gaston Villemure
Owner
Suite 310-7816 62 Avenue Edmonton, AB T5K 3M2
gaston@larkfielddwellings.ca
larkfielddwellings.ca
The blue colour used in the logo should be replicated and used within the stationary / business cards. Feel free to use additional complementary colours as well (including, but not limited to the grey colour used in the logo).. The intention is to have a modern feel but remain professional. The backside of the card can have designs but should allow some space to write notes.

```html
<!DOCTYPE html>
<html lang="en">
<head>
<meta charset="utf-8">
<title>Larkfield Dwellings Inc. – Business Cards</title>
<link href="https://fonts.googleapis.com/css2?family=Montserrat:wght@400;600;700&display=swap" rel="stylesheet">
<style>
  :root {
    --brand-blue: #2f5fb8;
    --brand-blue-light: #4a7fd6;
    --brand-blue-dark: #22489a;
    --brand-grey: #8a8d91;
    --ink: #4d4f53;
    --paper: #ffffff;
    --backdrop: #e9eaec;
  }
  html, body {
    margin: 0;
    padding: 0;
    width: 1200px;
    height: 901px;
    overflow: hidden;
    background: var(--backdrop);
    font-family: "Montserrat", Arial, sans-serif;
  }
  .canvas {
    position: relative;
    width: 1200px;
    height: 901px;
  }
  .card {
    position: absolute;
    width: 620px;
    height: 354px;
    border-radius: 18px;
    overflow: hidden;
    box-shadow: 0 8px 24px rgba(0,0,0,0.18);
  }
  /* Back of card */
  .card-back {
    left: 90px;
    top: 70px;
    background: linear-gradient(160deg, var(--brand-blue-light) 0%, var(--brand-blue) 55%, var(--brand-blue-dark) 100%);
    color: var(--paper);
  }
  .card-back .wordmark {
    position: absolute;
    left: 0;
    right: 0;
    top: 120px;
    text-align: center;
    font-weight: 700;
    font-size: 40px;
    letter-spacing: 0.5px;
    color: var(--paper);
  }
  .card-back .web {
    position: absolute;
    left: 0;
    right: 0;
    bottom: 40px;
    text-align: center;
    font-size: 17px;
    letter-spacing: 1.5px;
  }
  /* Front of card */
  .card-front {
    left: 490px;
    top: 470px;
    background: var(--paper);
  }
  .card-front .wordmark {
    position: absolute;
    left: 36px;
    top: 138px;
    width: 290px;
    display: flex;
    align-items: center;
    gap: 12px;
    font-weight: 700;
    font-size: 27px;
    line-height: 1.1;
    color: var(--brand-blue);
  }
  .wordmark .mark-square {
    flex: none;
    width: 16px;
    height: 16px;
    background: var(--brand-blue);
  }
  .card-front .divider {
    position: absolute;
    left: 352px;
    top: 76px;
    width: 2px;
    height: 126px;
    background: var(--brand-blue);
  }
  .contact {
    position: absolute;
    left: 368px;
    top: 72px;
    width: 240px;
    color: var(--ink);
    font-size: 12px;
    line-height: 1.45;
  }
  .contact .name {
    font-weight: 700;
    font-size: 16px;
    color: var(--brand-blue);
    margin: 0;
  }
  .contact .role {
    margin: 0 0 14px;
    color: var(--brand-grey);
    font-size: 13px;
  }
  .contact .address { margin: 0 0 12px; }
  .contact .lines { margin: 0; }
  .contact .label { color: var(--brand-blue); font-weight: 700; }
  .card-front .band {
    position: absolute;
    left: 0;
    bottom: 0;
    width: 100%;
    height: 46px;
  }
  .card-front .web {
    position: absolute;
    right: 30px;
    bottom: 14px;
    color: var(--paper);
    font-size: 14px;
    letter-spacing: 2px;
  }
</style>
</head>
<body>
<main class="canvas">
  <section class="card card-back" aria-label="Business card back">
    <div class="wordmark">Larkfield Dwellings</div>
    <div class="web">www.larkfielddwellings.ca</div>
  </section>

  <section class="card card-front" aria-label="Business card front">
    <div class="wordmark"><span class="mark-square"></span><span>Larkfield Dwellings</span></div>
    <div class="divider"></div>
    <div class="contact">
      <p class="name">Gaston Villemure</p>
      <p class="role">Owner</p>
      <p class="address">Suite 310-7816 62 Avenue<br>Edmonton, AB T5K 3M2</p>
      <p class="lines">
        <span class="label">P:</span> 780.555.0142<br>
        <span class="label">C:</span> 780.555.0187<br>
        <span class="label">E:</span> gaston@larkfielddwellings.ca
      </p>
    </div>
    <svg class="band" viewBox="0 0 620 46" preserveAspectRatio="none" aria-hidden="true">
      <polygon points="0,30 330,30 346,34 0,34" fill="var(--brand-blue)"/>
      <polygon points="330,30 620,30 620,46 0,46 0,34 346,34" fill="#ffffff"/>
      <polygon points="300,46 340,10 620,10 620,46" fill="var(--brand-grey)"/>
      <polygon points="0,38 300,38 296,42 0,42" fill="var(--brand-blue-light)"/>
    </svg>
    <div class="web">www.larkfielddwellings.ca</div>
  </section>
</main>
</body>
</html>
```